Lorn's Cleaners new delivery postcard

We need to advertise for our new pick up and delivery dry cleaning/laundry service.
Mens Business Shirts $2.00
Pants $4.50
Skirts $5.00
Dry Clean Shirt/Blouse $5.00
Dress $9.00
2 Piece Suits $9.00
Updates
We would like to use a 5x7 size postcard, printed on both sides. We would like to add a discount to the card for 25% off of their first order, with the flyer.
We are a famly run dry cleaners. My name is Paula Brandt and my cell # is 614-372-0481. We are trying to expand our business to include free pick and delivery.
If possible can you use the logo I sent some where on the postcard? The phone # for the store is 614-205-3967.
Reason: Still need to get partners approval.
Industry/Entity Type
Business

```html
<!DOCTYPE html>
<html lang="en">
<head>
<meta charset="utf-8">
<title>Lorn's Cleaners – New Delivery Postcard</title>
<link href="https://fonts.googleapis.com/css2?family=Roboto:wght@400;500;700&display=swap" rel="stylesheet">
<style>
  :root {
    --stage: #3a3a3c;
    --paper: #ffffff;
    --blue: #1f63b0;
    --sky: #2aa7df;
    --orange: #f5a623;
    --orange-deep: #ef8a1c;
    --red: #d8401e;
    --ink: #333333;
    --rule: #9a9a9a;
  }
  * { margin: 0; padding: 0; box-sizing: border-box; }
  html, body { width: 807px; height: 1200px; overflow: hidden; }
  body {
    background: var(--stage);
    font-family: "Roboto", Arial, sans-serif;
    position: relative;
  }
  .postcard {
    position: absolute;
    left: 53px;
    width: 700px;
    height: 500px;
    background: var(--paper);
    overflow: hidden;
    box-shadow: 0 6px 18px rgba(0,0,0,.45);
  }
  .postcard--front { top: 70px; }
  .postcard--back { top: 630px; }
  .shapes { position: absolute; inset: 0; width: 700px; height: 500px; }

  /* front */
  .front-photo {
    position: absolute; left: 0; top: 0; width: 700px; height: 310px;
    background: linear-gradient(120deg, #c9d3dc 0%, #7d8a99 45%, #3d4654 75%, #a9b4c2 100%);
  }
  .headline {
    position: absolute; left: 40px; top: 318px;
    color: var(--blue); font-weight: 700; line-height: 1.12;
    font-size: 44px; text-align: right;
  }
  .badge {
    position: absolute; left: 510px; top: 270px; width: 170px; height: 170px;
    border-radius: 50%; background: var(--red);
    border: 6px solid #fff; box-shadow: 0 3px 8px rgba(0,0,0,.3);
    color: #fff; text-align: center; font-weight: 700;
    display: flex; flex-direction: column; justify-content: center;
  }
  .badge__amount { font-size: 50px; line-height: 1; }
  .badge__amount small { font-size: 20px; vertical-align: top; }
  .badge__label { font-size: 30px; margin-top: 4px; }

  /* back */
  .back-photo {
    position: absolute; left: 28px; top: 28px; width: 220px; height: 160px;
    background: linear-gradient(135deg, #5aa0d8 0%, #d85a6a 45%, #e8c9a0 70%, #6d8fb5 100%);
  }
  .contact {
    position: absolute; left: 272px; top: 118px; color: #fff;
  }
  .contact__name { font-size: 27px; font-weight: 400; white-space: nowrap; }
  .contact__phone { font-size: 17px; margin-top: 6px; display: flex; align-items: center; gap: 6px; }
  .service-title {
    position: absolute; left: 28px; top: 228px;
    color: var(--orange-deep); font-size: 24px; line-height: 1.25; font-weight: 400;
  }
  .price-list {
    position: absolute; left: 28px; top: 312px; width: 300px; list-style: none;
    font-size: 14px; color: var(--blue);
  }
  .price-list li { display: flex; align-items: baseline; line-height: 1.62; }
  .price-list .leader { flex: 1; border-bottom: 1px dotted var(--blue); margin: 0 4px; }
  .price-list .price { color: var(--orange-deep); }
  .stamp-box {
    position: absolute; left: 560px; top: 92px; width: 48px; height: 56px;
    border: 1.5px solid var(--ink);
  }
  .address-line {
    position: absolute; left: 450px; width: 200px; border-top: 1.5px solid var(--rule);
  }
</style>
</head>
<body>

<section class="postcard postcard--front">
  <div class="front-photo" role="img" aria-label="Photo of a dry cleaner employee holding a suit jacket on a hanger"></div>
  <svg class="shapes" viewBox="0 0 700 500" aria-hidden="true">
    <path d="M0 300 C200 360 420 240 700 250 L700 500 L0 500 Z" fill="#ffffff"/>
    <path d="M0 268 C230 330 430 225 700 225 L700 262 C430 262 230 360 0 310 Z" fill="var(--sky)"/>
    <path d="M0 430 C120 420 220 460 330 500 L0 500 Z" fill="var(--orange)"/>
    <path d="M430 500 C540 440 620 420 700 420 L700 500 Z" fill="var(--orange)"/>
  </svg>
  <h1 class="headline">Lorn's Cleaners<br>New Delivery</h1>
  <div class="badge">
    <div class="badge__amount">25%<small> off</small></div>
    <div class="badge__label">Discount</div>
  </div>
</section>

<section class="postcard postcard--back">
  <svg class="shapes" viewBox="0 0 700 500" aria-hidden="true">
    <path d="M420 0 L700 0 L700 70 C600 40 500 30 420 0 Z" fill="var(--orange)"/>
    <path d="M150 100 C270 90 380 95 480 68 L480 195 C380 205 270 212 150 205 Z" fill="var(--sky)"/>
    <path d="M0 205 C160 215 320 205 480 172 L480 197 C320 232 160 240 0 232 Z" fill="var(--orange)"/>
    <path d="M0 470 C150 455 300 480 400 500 L0 500 Z" fill="var(--orange)"/>
    <line x1="430" y1="230" x2="430" y2="470" stroke="#dddddd" stroke-width="1"/>
  </svg>
  <div class="back-photo" role="img" aria-label="Photo of a laundry basket beside folded stacks of clothes"></div>
  <div class="contact">
    <div class="contact__name">Paula Brandt</div>
    <div class="contact__phone">
      <svg width="14" height="16" viewBox="0 0 14 16" aria-hidden="true"><rect x="2" y="0.5" width="10" height="15" rx="2" fill="#fff"/><rect x="4" y="2.5" width="6" height="8" fill="var(--sky)"/></svg>
      614-372-0481
    </div>
  </div>
  <h2 class="service-title">Our New Pick Up &amp; Delivery<br>Dry Cleaning/Laundry Service</h2>
  <ul class="price-list">
    <li><span>Mens Business Shirts</span><span class="leader"></span><span class="price">$2.00</span></li>
    <li><span>Pants</span><span class="leader"></span><span class="price">$4.50</span></li>
    <li><span>Skirts</span><span class="leader"></span><span class="price">$5.00</span></li>
    <li><span>Dry Clean Shirt/Blouse</span><span class="leader"></span><span class="price">$5.00</span></li>
    <li><span>Dress</span><span class="leader"></span><span class="price">$9.00</span></li>
    <li><span>2 Piece Suits</span><span class="leader"></span><span class="price">$9.00</span></li>
  </ul>
  <div class="stamp-box"></div>
  <div class="address-line" style="top:310px"></div>
  <div class="address-line" style="top:345px"></div>
  <div class="address-line" style="top:380px"></div>
</section>

</body>
</html>
```